www.valmorlinkgroup.example Redesign

The current website was designed 2 - 3 years ago, and we feel it is a bit outdated and bland. We would like to get a new design implement, which is fresh and shows our business/network in a professional manner.

It is important for the site to emphasize that we are a European specialist in our market, Specialist logistics, so we would very much like this emphasized with a European map feature on the main page.

Open to suggestions on how this is done, and appreciate your efforts.

Please visit our existing website at www.valmorlinkgroup.example to understand more about the business to aide the design.

I have loads more images should you want more to look at, you may need the rest of the data when the rest of the pages are designed etc.

Target Market(s)

We provide speclist logistics / freight services to a host of industries including but not limited to - HealthCare, Banking & Retail, Vending & Gaming, Fitness, Access Control, Power, Data and Office print. So we need to show diversity and that we can flex to customer needs.

Industry/Entity Type

Logistics

Font styles to use
Sans Serif

Colors
0555a3
34a7d8
959595
ffffff

Requirements
Must have
• - European Map emphasizing European capabilities
• - On each partner page a smaller version of the European map showing the countries they cover (this info is shown in the text provided)
• - Business sectors brief similar to current website on opening page showing industries we support (dont have to use provided logos - happy for you to provide new content)
• - Must be an easy link on each and every page for the customer to click and submit an inquiry (info@valmorlinkgroup.example)
Nice to have
• - Interactive European Map - so the user can click on the country and it takes them to the service partners page that managers that country. ie - if they click on UK it takes them to the UK Partner = Kestova Brandwell UK
• - Clean site not too busy
• - Prefer to have larger images and less text
Should not have
• - Too much white - unless you can keep it fresh (Current website design has lots of white background and looks bland)

```html
<!DOCTYPE html>
<html lang="en">
<head>
<meta charset="utf-8">
<title>Valmorlink – Global Network for High Tech Services &amp; Logistics</title>
<link href="https://fonts.googleapis.com/css2?family=Roboto:wght@300;400;500;700;900&family=Open+Sans:wght@400;600&display=swap" rel="stylesheet">
<style>
:root{
  --blue:#0555a3;
  --blue-dark:#043f7a;
  --sky:#34a7d8;
  --grey:#959595;
  --grey-light:#e9eaec;
  --ink:#2b2b2b;
  --footer:#141516;
  --white:#ffffff;
}
*{box-sizing:border-box;margin:0;padding:0}
html,body{width:1200px;height:4128px;overflow:hidden}
body{font-family:"Open Sans",Arial,sans-serif;color:var(--ink);background:var(--white);position:relative}
h1,h2,h3,h4,.nav,.btn{font-family:"Roboto",Arial,sans-serif}
.abs{position:absolute}

/* header */
.site-header{position:absolute;top:0;left:0;width:1200px;height:120px;background:var(--white)}
.brand{position:absolute;left:100px;top:36px;display:flex;align-items:center;gap:12px;font-family:"Roboto",sans-serif;font-weight:900;font-size:44px;color:var(--blue);letter-spacing:1px}
.brand i{display:block;width:16px;height:16px;background:var(--sky)}
.call{position:absolute;left:630px;top:38px;display:flex;align-items:center;gap:12px}
.call svg{width:30px;height:30px}
.call small{display:block;font-size:13px;color:var(--grey)}
.call strong{font-family:"Roboto",sans-serif;font-size:19px;color:var(--ink)}
.search{position:absolute;left:900px;top:44px;width:200px;height:32px;border:1px solid #ccc;font-size:13px;color:#aaa;padding:6px 10px}

.nav{position:absolute;top:120px;left:0;width:1200px;height:48px;background:var(--blue);display:flex;padding-left:100px}
.nav a{color:var(--white);text-decoration:none;font-size:15px;font-weight:500;line-height:48px;padding:0 22px}
.nav a.active{background:var(--blue-dark)}

/* hero */
.hero{position:absolute;top:168px;left:0;width:1200px;height:492px;background:linear-gradient(120deg,#6d7a86 0%,#3c4b57 45%,#2d3a45 100%)}
.hero-title{position:absolute;top:370px;width:1200px;text-align:center;color:var(--white);font-weight:900;font-size:40px;line-height:48px;text-transform:uppercase}
.btn{display:inline-block;background:var(--blue);color:var(--white);font-size:14px;font-weight:500;padding:10px 26px;text-transform:uppercase;letter-spacing:.5px}
.hero-btn{position:absolute;top:488px;left:540px}

/* service cards */
.cards{position:absolute;top:660px;left:100px;width:1000px;display:flex;gap:16px}
.card{width:238px;height:300px;background:var(--blue);position:relative}
.card .photo{height:130px}
.card .icon{position:absolute;top:108px;left:97px;width:44px;height:44px;border-radius:50%;background:var(--sky);border:3px solid var(--white)}
.card .icon svg{width:38px;height:38px}
.card h3{margin-top:34px;text-align:center;color:var(--white);font-size:18px;font-weight:700;text-transform:uppercase}
.card p{color:#cfe0f1;font-size:12px;line-height:18px;text-align:center;padding:8px 18px 0}

/* about */
.section-title{position:absolute;width:1200px;text-align:center;font-size:32px;font-weight:700;text-transform:uppercase}
.section-title::after{content:"";display:block;width:60px;height:3px;background:var(--sky);margin:12px auto 0}
.about-text{position:absolute;left:160px;width:880px;text-align:center;font-size:14px;line-height:22px;color:#555}
.about-sub{position:absolute;top:1128px;width:1200px;text-align:center;font-family:"Roboto",sans-serif;font-size:20px;font-weight:700;color:var(--ink)}

/* sectors */
.sectors{position:absolute;top:1380px;left:0;width:1200px;height:720px;background:var(--grey-light)}
.sectors-intro{position:absolute;top:1500px;width:1200px;text-align:center;font-size:15px;color:#555}
.hub{position:absolute;left:440px;top:1620px;width:320px;height:320px}
.sector{position:absolute;width:330px}
.sector h4{font-size:21px;font-weight:700;color:var(--blue);margin-bottom:6px}
.sector p{font-size:12px;line-height:18px;color:#555}
.sector.left{text-align:right;left:90px;padding-right:76px}
.sector.right{left:780px;padding-left:76px}
.sector .badge{position:absolute;top:0;width:58px;height:58px;border-radius:50%;background:var(--white);border:2px solid var(--blue)}
.sector.left .badge{right:0}
.sector.right .badge{left:0}
.badge svg{width:54px;height:54px}

/* banner */
.banner{position:absolute;top:2100px;left:0;width:1200px;height:440px;background:linear-gradient(180deg,#1b5ea8 0%,#0e4a8e 55%,#0a3f7c 100%)}
.banner-title{position:absolute;top:2215px;width:1200px;text-align:center;color:var(--white);font-size:58px;font-weight:300;line-height:66px}
.banner-text{position:absolute;top:2360px;left:260px;width:680px;text-align:center;color:#d8e6f4;font-size:13px;line-height:20px}
.banner-btn{position:absolute;top:2440px;left:540px;background:transparent;border:2px solid var(--white)}

/* news */
.news{position:absolute;top:2690px;left:100px;width:1000px;display:flex;gap:34px}
.post{width:310px}
.post .photo{height:200px;position:relative}
.post .date{position:absolute;top:0;left:14px;width:52px;background:var(--blue);color:var(--white);text-align:center;font-family:"Roboto",sans-serif;padding:6px 0}
.post .date b{display:block;font-size:20px}
.post .date span{font-size:11px;text-transform:uppercase}
.post h4{margin-top:18px;font-size:17px;font-weight:500;white-space:nowrap;overflow:hidden;text-overflow:ellipsis}
.post p{margin-top:10px;font-size:13px;line-height:20px;color:#666}
.post a{display:block;margin-top:10px;font-family:"Roboto",sans-serif;font-size:13px;font-weight:700;color:var(--blue);text-decoration:none;text-transform:uppercase}

.map{position:absolute;top:3100px;left:0;width:1200px;height:420px;background:radial-gradient(ellipse at 50% 45%,#d6d8db 0%,#c3c6ca 60%,#b6b9bd 100%)}
.partners{position:absolute;top:3520px;left:0;width:1200px;height:140px;background:#f4f4f4;display:flex;justify-content:center;align-items:center;gap:52px}
.partners span{display:block;width:124px;height:40px;background:#bdbdbd;border-radius:4px}

/* footer */
.footer{position:absolute;top:3660px;left:0;width:1200px;height:420px;background:var(--footer);color:#ccc}
.footer h4{position:absolute;top:40px;color:var(--white);font-size:20px;font-weight:500;text-transform:uppercase}
.links{position:absolute;top:100px;left:100px;list-style:none}
.links li{font-size:13px;line-height:26px}
.links li::before{content:"› ";color:var(--sky)}
.footer .brand{top:300px;font-size:34px;color:var(--white)}
.quote{position:absolute;top:96px;left:380px;width:380px}
.field{height:34px;background:var(--white);margin-bottom:10px;font-size:12px;color:#999;padding:8px 10px}
.field.tall{height:84px}
.quote .btn{display:block;width:160px;margin:6px auto 0;text-align:center}
.contact{position:absolute;top:100px;left:820px;width:290px;font-size:13px;line-height:20px}
.contact div{display:flex;gap:14px;margin-bottom:18px}
.contact svg{flex:none;width:18px;height:18px}
.socials{display:flex;gap:10px}
.socials span{width:28px;height:28px;border-radius:50%;border:1px solid #888}
.copyright{position:absolute;top:4080px;left:0;width:1200px;height:48px;background:#0b0b0c;color:#aaa;text-align:center;font-size:12px;line-height:48px}
</style>
</head>
<body>

<header class="site-header">
  <div class="brand"><i></i>VALMORLINK</div>
  <div class="call">
    <svg viewBox="0 0 24 24"><path fill="#555" d="M6.6 10.8c1.4 2.8 3.8 5.1 6.6 6.6l2.2-2.2c.3-.3.7-.4 1-.2 1.1.4 2.3.6 3.6.6.6 0 1 .4 1 1V20c0 .6-.4 1-1 1C10.6 21 3 13.4 3 4c0-.6.4-1 1-1h3.5c.6 0 1 .4 1 1 0 1.3.2 2.5.6 3.6.1.3 0 .7-.2 1z"/></svg>
    <div><small>Call Us :</small><strong>900-555-0142</strong></div>
  </div>
  <div class="search">Search here</div>
</header>

<nav class="nav">
  <a class="active">HOME</a><a>ABOUT US</a><a>BUSINESS SECTORS</a><a>SERVICES</a><a>NETWORK</a><a>BLOG</a><a>CONTACT US</a>
</nav>

<section class="hero" role="img" aria-label="Photo of a logistics truck being loaded outside a warehouse"></section>
<h1 class="hero-title">The Leading Global Network<br>for High Tech Services &amp; Logistics</h1>
<span class="btn hero-btn">Read More</span>

<div class="cards">
  <div class="card">
    <div class="photo" role="img" aria-label="Photo of a delivery truck" style="background:linear-gradient(135deg,#8a97a3,#55636f)"></div>
    <div class="icon"><svg viewBox="0 0 38 38"><path fill="#fff" d="M7 14h15v10H7zM22 17h5l4 4v3h-9z"/><circle cx="12" cy="26" r="2.5" fill="#fff"/><circle cx="27" cy="26" r="2.5" fill="#fff"/></svg></div>
    <h3>Transport</h3>
    <p>Valmorlink partners move specialist equipment across Europe with trained crews and dedicated vehicles.</p>
  </div>
  <div class="card">
    <div class="photo" role="img" aria-label="Photo of warehouse shelving with stock" style="background:linear-gradient(135deg,#9a8f7d,#5f5a52)"></div>
    <div class="icon"><svg viewBox="0 0 38 38"><path fill="#fff" d="M8 16l11-6 11 6v12h-4V18H12v10H8z"/><path fill="#fff" d="M14 20h10v3H14zM14 24h10v3H14z"/></svg></div>
    <h3>Warehousing</h3>
    <p>Secure storage facilities in every country to meet customer demand for stock and project staging.</p>
  </div>
  <div class="card">
    <div class="photo" role="img" aria-label="Photo of a technician installing equipment" style="background:linear-gradient(135deg,#6f8aa0,#3e5266)"></div>
    <div class="icon"><svg viewBox="0 0 38 38"><path fill="none" stroke="#fff" stroke-width="3" d="M11 27l10-10M24 10a5 5 0 1 0 4 4l-4 1-1-4z"/></svg></div>
    <h3>Technical Services</h3>
    <p>Installation, configuration and removal services carried out by engineers across the network.</p>
  </div>
  <div class="card">
    <div class="photo" role="img" aria-label="Photo of a worker handling returned goods" style="background:linear-gradient(135deg,#a28a72,#5b5048)"></div>
    <div class="icon"><svg viewBox="0 0 38 38"><path fill="none" stroke="#fff" stroke-width="3" d="M12 18a8 8 0 1 1 2 7"/><path fill="#fff" d="M8 15l5 6 4-6z"/></svg></div>
    <h3>Returns</h3>
    <p>Responsible end-of-life collection and return of equipment with full recycling reporting.</p>
  </div>
</div>

<h2 class="section-title" style="top:990px">About Our Company</h2>
<p class="about-text" style="top:1058px">Valmorlink leads the way in specialist technical logistics, having identified the best in class partners and established exclusive relationships with these companies. Valmorlink exists to deliver the following core values.</p>
<h3 class="about-sub">No1 Global High Tech Logistics Network</h3>
<p class="about-text" style="top:1168px">With each partner you benefit from the expertise, competitive advantage, service and a local presence, whilst being able to enjoy the benefit of a consistent high service level across the countries. Every partner is a market leader in their own region and brings in local characteristics, whilst being engaged as a partner in the leading network for technical distribution services. A guaranteed end-to-end solution. This supports the geographical reach and depths of the total supply chain, from pre-installation to distribution and on-site installation of your finished products through to recycling and reverse logistics services.</p>

<section class="sectors"></section>
<h2 class="section-title" style="top:1440px">Business Sectors</h2>
<p class="sectors-intro">Valmorlink offers Global specialist logistics across a number of high tech sectors</p>

<svg class="hub" viewBox="0 0 320 320" role="img" aria-label="Illustration of a network globe inside a half gear, half blue circle">
  <defs><linearGradient id="hubFill" x1="0" x2="1"><stop offset="0" stop-color="#7b8591"/><stop offset=".5" stop-color="#7b8591"/><stop offset=".5" stop-color="#0f66c0"/><stop offset="1" stop-color="#0555a3"/></linearGradient></defs>
  <circle cx="160" cy="160" r="158" fill="url(#hubFill)"/>
  <circle cx="160" cy="160" r="104" fill="#d7dde3"/>
</svg>

<div class="sector left" style="top:1620px"><span class="badge"><svg viewBox="0 0 54 54"><path fill="#0555a3" d="M23 15h8v8h8v8h-8v8h-8v-8h-8v-8h8z"/></svg></span><h4>HealthTech</h4><p>Here in the HealthTech sector, the Valmorlink partners are experienced experts in delivering specialist equipment.</p></div>
<div class="sector left" style="top:1750px"><span class="badge"><svg viewBox="0 0 54 54"><rect x="18" y="13" width="18" height="28" rx="2" fill="none" stroke="#0555a3" stroke-width="3"/><rect x="22" y="18" width="10" height="8" fill="#0555a3"/></svg></span><h4>Vending &amp; Gaming</h4><p>Our extensive Valmorlink network provides full coverage for installation and maintenance services.</p></div>
<div class="sector left" style="top:1880px"><span class="badge"><svg viewBox="0 0 54 54"><path fill="#0555a3" d="M12 22l15-9 15 9zM15 24h4v12h-4zM25 24h4v12h-4zM35 24h4v12h-4zM12 38h30v3H12z"/></svg></span><h4>Banking &amp; Retail</h4><p>Trusted provider of banking and retail logistics, including the delivery and commissioning of kiosks.</p></div>

<div class="sector right" style="top:1620px"><span class="badge"><svg viewBox="0 0 54 54"><path fill="#0555a3" d="M14 23h4v8h-4zM18 20h4v14h-4zM22 25h10v4H22zM32 20h4v14h-4zM36 23h4v8h-4z"/></svg></span><h4>Fitness</h4><p>For the dynamic fitness, wellness and lifestyle market we deliver and install gym equipment.</p></div>
<div class="sector right" style="top:1750px"><span class="badge"><svg viewBox="0 0 54 54"><rect x="17" y="25" width="20" height="15" rx="2" fill="#0555a3"/><path fill="none" stroke="#0555a3" stroke-width="3" d="M21 25v-5a6 6 0 0 1 12 0v5"/></svg></span><h4>Access control</h4><p>Valmorlink partners have experience of major project roll-outs of access control systems.</p></div>
<div class="sector right" style="top:1880px"><span class="badge"><svg viewBox="0 0 54 54"><path fill="#0555a3" d="M29 11l-12 18h9l-3 14 13-19h-9z"/></svg></span><h4>Power</h4><p>Power is the key element linking the high tech sectors; we handle heavy units with care.</p></div>

<section class="banner" role="img" aria-label="Warehouse interior photo with a blue tint"></section>
<h2 class="banner-title">Valmorlink Provide Advanced<br>Technical Logistics Services</h2>
<p class="banner-text">Sed ut perspiciatis unde omnis iste natus error sit voluptatem accusantium doloremque laudantium, totam rem aperiam, eaque ipsa quae ab illo inventore veritatis et quasi architecto beatae vitae dicta sunt explicabo.</p>
<span class="btn banner-btn">Read More</span>

<h2 class="section-title" style="top:2610px">Latest News</h2>
<div class="news">
  <article class="post">
    <div class="photo" role="img" aria-label="Photo of a conference stage at the company summit" style="background:linear-gradient(135deg,#3a3a3a,#1c1c1c)"><div class="date"><b>02</b><span>Jun</span></div></div>
    <h4>Valmorlink Summit 2016</h4>
    <p>This year's annual Valmorlink summit was held in Dublin. There was good representation from the European partners along with our award.</p>
    <a>Read More</a>
  </article>
  <article class="post">
    <div class="photo" role="img" aria-label="Photo of two new delivery trucks" style="background:linear-gradient(135deg,#6b6f73,#2f3337)"><div class="date"><b>02</b><span>Jun</span></div></div>
    <h4>Norvane Freight adds 2 new trucks</h4>
    <p>Good news from our UK partner. Norvane Freight Solutions added two new 7.5 tonne trucks to their fleet. The trucks have been designed.</p>
    <a>Read More</a>
  </article>
  <article class="post">
    <div class="photo" role="img" aria-label="Photo of a presentation on stage" style="background:linear-gradient(135deg,#5a3b3b,#1f1a1a)"><div class="date"><b>02</b><span>Jun</span></div></div>
    <h4>Successful presentation of Valmorlink</h4>
    <p>This year's annual Valmorlink summit was held in Dublin. There was good representation from the European partners along with our award.</p>
    <a>Read More</a>
  </article>
</div>

<section class="map" role="img" aria-label="Grey world map highlighting the European partner network"></section>

<section class="partners" aria-label="Partner companies">
  <span></span><span></span><span></span><span></span><span></span><span></span>
</section>

<footer class="footer">
  <h4 style="left:100px">Quick Links</h4>
  <ul class="links">
    <li>Home</li><li>About</li><li>Business Sectors</li><li>Services</li><li>Contact Us</li><li>Network</li>
  </ul>
  <div class="brand" style="left:100px"><i></i>VALMORLINK</div>

  <h4 style="left:380px">Get a Quote</h4>
  <form class="quote">
    <div class="field">Name</div>
    <div class="field">Address</div>
    <div class="field">Email</div>
    <div class="field tall">Comments</div>
    <span class="btn">Send Form</span>
  </form>

  <h4 style="left:820px">Contact Us</h4>
  <div class="contact">
    <div><svg viewBox="0 0 24 24"><path fill="#34a7d8" d="M12 2a7 7 0 0 0-7 7c0 5 7 13 7 13s7-8 7-13a7 7 0 0 0-7-7zm0 9.5A2.5 2.5 0 1 1 12 6.5a2.5 2.5 0 0 1 0 5z"/></svg><span>Valmorlink<br>48 Harbour Lane, Northgate</span></div>
    <div><svg viewBox="0 0 24 24"><path fill="#34a7d8" d="M6.6 10.8c1.4 2.8 3.8 5.1 6.6 6.6l2.2-2.2c.3-.3.7-.4 1-.2 1.1.4 2.3.6 3.6.6.6 0 1 .4 1 1V20c0 .6-.4 1-1 1C10.6 21 3 13.4 3 4c0-.6.4-1 1-1h3.5c.6 0 1 .4 1 1 0 1.3.2 2.5.6 3.6.1.3 0 .7-.2 1z"/></svg><span>Phone<br>900-555-0142</span></div>
    <div><svg viewBox="0 0 24 24"><path fill="#34a7d8" d="M3 5h18v14H3zm2 2v1l7 5 7-5V7l-7 5z"/></svg><span>info@valmorlinkgroup.example</span></div>
    <div class="socials"><span></span><span></span><span></span><span></span></div>
  </div>
</footer>
<div class="copyright">Copyright © Valmorlink 2017. All rights reserved.</div>

</body>
</html>
```